Corporate Profile, with ALOT more work for winning bidder

We need
1. CD designed
2. CD Cover Designed
3. 2x Envelope's designed
4. Letter head designed
The designer picked will also get many further projects from us. Almost totaling 10k a year.
- More info
• Software installation disc
a. Logo
b. Contact details (See below)
c. Instructions
o “Please insert CD into computer and follow the prompts”
d. Title
o “Free Software Installation Disc”
• CD Sleave double sided
- Front
o Logo
o Website Address
o Facebook address
o Title
? “Free Software Installation Disc”
• Letter head
- Logo
- Contact information
- A4 paper size
• C4 Envelope
- Nicely Designed with logo
- A window to put address
- Printed return address (See below) on back
• DL Envelope, to return to us
- Had our return address ( See below)
- Nice design
Contact details
Pixel Harbour Co
17b Tamsin Crescent Kellerton, Vic, 3188
www.PixelHarbourCo.com.au
1300 42 19 58
www.Chatterloop.com/PixelHarbourCo
Return Address
Pixel Harbour Co
17b Tamsin Crescent
Kellerton, Vic, 3188

```html
<!DOCTYPE html>
<html lang="en">
<head>
<meta charset="utf-8">
<title>Pixel Harbour Co — Letterhead</title>
<link rel="stylesheet" href="https://fonts.googleapis.com/css2?family=Arimo:wght@400;700&display=swap">
<style>
  :root {
    --brand-blue: #1c7fd4;
    --paper: #ffffff;
    --ink: #1a1a1a;
    --backdrop: #ffffff;
    --mark: #5fc6ef;
  }
  html, body {
    margin: 0;
    width: 1200px;
    height: 900px;
    overflow: hidden;
    background: var(--backdrop);
  }
  .letterhead {
    position: absolute;
    left: 348px;
    top: 88px;
    width: 500px;
    height: 707px;
    background: var(--paper);
    box-shadow: 3px 3px 5px rgba(0, 0, 0, 0.45);
  }
  .letterhead svg {
    display: block;
    font-family: "Arimo", Arial, sans-serif;
  }
  .band { fill: var(--brand-blue); }
  .cutout { fill: var(--paper); }
  .header-link {
    fill: var(--paper);
    font-weight: 700;
  }
  .brand-name {
    fill: var(--ink);
    font-weight: 700;
    font-size: 13px;
  }
  .brand-square { fill: var(--mark); }
  .footer-phone {
    fill: var(--ink);
    font-weight: 700;
    font-size: 11.5px;
  }
  .footer-address {
    fill: var(--ink);
    font-size: 9.5px;
  }
</style>
</head>
<body>
  <div class="letterhead">
    <svg width="500" height="707" viewBox="0 0 500 707" xmlns="http://www.w3.org/2000/svg">
      <defs>
        <clipPath id="page-clip">
          <rect x="0" y="0" width="500" height="707"/>
        </clipPath>
      </defs>
      <g clip-path="url(#page-clip)">
        <rect class="band" x="0" y="0" width="500" height="83"/>
        <circle class="cutout" cx="249" cy="-61" r="140"/>

        <rect class="brand-square" x="232" y="8" width="34" height="34" rx="3"/>
        <text class="brand-name" x="249" y="62" text-anchor="middle">Pixel Harbour Co</text>

        <text class="header-link" x="6" y="75" font-size="8.2">www.Chatterloop.com/PixelHarbourCo</text>
        <text class="header-link" x="495" y="74" font-size="10" text-anchor="end">www.PixelHarbourCo.com.au</text>

        <rect class="band" x="0" y="638" width="500" height="69"/>
        <circle class="cutout" cx="248" cy="788" r="143"/>

        <text class="footer-phone" x="248" y="666" text-anchor="middle">1300 42 19 58</text>
        <text class="footer-address" x="248" y="684" text-anchor="middle">Pixel Harbour Co</text>
        <text class="footer-address" x="248" y="697" text-anchor="middle">17b Tamsin Crescent Kellerton, Vic, 3188</text>
      </g>
    </svg>
  </div>
</body>
</html>
```